Redesign of an educational Eye website for Medical Students and Healthcare professionals

www.corvantisportal.com is an educational resource, illustrated using high quality 3D animations, for undergraduate medical students and healthcare professionals to learn about the anatomy of the human eye and associated common eye disorders.

The website was originally developed (using a Joomla template) a couple of years ago and we now want to update the brand and design of the site. Example content and animations can be found at https://www.corvantisportal.com/overview or https://www.corvantisportal.com/ocular-anatomy/orbital-anatomy

We would like a new logo and home page design (to include new colour palette, fonts and updated overall design).

The attached PowerPoint contains an example layout of the revised components we want to appear on the new Home page. We plan to have a hero panel at the top of page playing a short video of some of the animations. Similar to how this site works (www.zembri.uk.com).

We want the new site to feel Professional, Modern and Clean and simple.

Target Market(s)

Undergraduate medical students and Healthcare Professionals

Industry/Entity Type

Medical

Logo Text

Corvantis Portal

Number of Pages Required

1 page

Font styles to use
Sans Serif

Colors

Designer to choose colors to be used in the design.

```html
<!DOCTYPE html>
<html lang="en">
<head>
<meta charset="utf-8">
<title>Corvantis Portal</title>
<link href="https://fonts.googleapis.com/css2?family=Montserrat:wght@400;500;600;700&family=Cabin:wght@400&family=Libre+Baskerville&display=swap" rel="stylesheet">
<style>
:root{
  --teal:#1b93a0;
  --ink:#222a30;
  --hero-blue:#2c5b98;
  --hero-teal:#3da3b4;
  --white:#ffffff;
  --label:#c9d7e6;
  --label-line:#d6e2ee;
  --grey:#8a8a8a;
  --rule:#e3e3e3;
}
*{margin:0;padding:0;box-sizing:border-box}
html,body{width:1200px;height:749px;overflow:hidden;background:var(--white);font-family:'Montserrat',sans-serif}
.page{position:relative;width:1200px;height:749px;overflow:hidden}
.site-header{position:absolute;left:0;top:0;width:1200px;height:147px}
.brand{position:absolute;left:171px;top:36px;display:flex;align-items:center;gap:14px;color:var(--teal);font-weight:700;letter-spacing:2px}
.brand-mark{width:16px;height:16px;border-radius:50%;background:var(--teal)}
.brand-name{font-size:40px;line-height:1}
.sign-in{position:absolute;left:934px;top:80px;font-size:22px;font-weight:500;color:var(--ink);display:flex;align-items:center;gap:8px;text-decoration:none;letter-spacing:-.5px}
.hero{position:absolute;left:0;top:147px;width:1200px;height:470px;background:linear-gradient(90deg,var(--hero-blue) 0%,#3570a8 45%,var(--hero-teal) 100%);overflow:hidden}
.hero-stripe{position:absolute;left:0;top:0;width:100%;height:3px;background:linear-gradient(90deg,#5a7fb0,#7cc4d0)}
.hero-visual{position:absolute;left:330px;top:0;width:600px;height:470px;background:radial-gradient(ellipse 50% 55% at 50% 52%,#8a7a5a 0%,#6c7d86 45%,rgba(90,130,170,.4) 75%,rgba(60,110,170,0) 100%)}
.label-panel{position:absolute;width:198px;background:rgba(255,255,255,.06);padding:0 6px}
.label-panel.right{width:192px}
.label{display:block;font-family:'Cabin',sans-serif;font-size:20px;color:var(--label);border-bottom:2px solid rgba(214,226,238,.6);padding:4px 10px 3px}
.hero-copy{position:absolute;left:392px;top:70px;width:432px;text-align:center;color:var(--white)}
.hero-title{font-size:22px;font-weight:700;letter-spacing:.3px;margin-bottom:16px}
.hero-text{font-size:12.5px;line-height:24px}
.cta{position:absolute;left:474px;width:267px;height:59px;border:1px solid var(--white);color:var(--white);text-align:center;padding-top:13px;font-size:14.5px;line-height:17px;text-decoration:none}
.cta strong{display:block;font-weight:700;font-size:14px}
.trusted{position:absolute;left:183px;top:630px;width:848px;display:flex;align-items:center;gap:10px}
.trusted-rule{flex:1;height:1px;background:var(--rule)}
.trusted-label{font-size:6px;color:#b8b8b8;letter-spacing:.5px}
.partners{position:absolute;left:0;top:660px;width:1200px;height:89px}
.partner{position:absolute;display:flex;align-items:center;gap:10px;color:var(--grey);font-family:'Montserrat',sans-serif;font-size:15px;font-weight:500;line-height:1.2}
.partner-mark{flex:none;width:40px;height:40px;background:#b5b5b5}
.partner-mark.round{border-radius:50%}
</style>
</head>
<body>
<div class="page">
  <header class="site-header">
    <div class="brand"><span class="brand-mark"></span><span class="brand-name">CORVANTIS PORTAL</span></div>
    <a class="sign-in" href="#">SIGN IN
      <svg width="28" height="14" viewBox="0 0 28 14"><path d="M0 7H24M18 1L25 7L18 13" fill="none" stroke="#222a30" stroke-width="3"/></svg>
    </a>
  </header>

  <section class="hero">
    <div class="hero-stripe"></div>
    <div class="hero-visual" role="img" aria-label="Cross-section animation of the human eye showing lens, retina and optic nerve"></div>

    <div class="label-panel" style="left:10px;top:23px">
      <span class="label">Limbus</span><span class="label">Cornea</span><span class="label">Iris</span><span class="label">Lens</span><span class="label">Pupil</span>
    </div>
    <div class="label-panel" style="left:10px;top:301px">
      <span class="label">Anterior Chamber</span><span class="label">Zonules</span><span class="label">Drainage Angle</span><span class="label">Ciliary Body</span><span class="label">Ciliary Muscle</span>
    </div>
    <div class="label-panel right" style="left:1008px;top:26px">
      <span class="label">Superior Rectus Muscle</span><span class="label">Sclera</span><span class="label">Choroid</span><span class="label">Retina</span><span class="label">Macula</span>
    </div>
    <div class="label-panel right" style="left:1010px;top:287px">
      <span class="label">Central Retinal Artery</span><span class="label">Optic Disc</span><span class="label">Fovea</span><span class="label">Retinal Blood Vessels</span><span class="label">Vitreous body</span>
    </div>

    <div class="hero-copy">
      <h1 class="hero-title">LEARN FASTER AND SMARTER</h1>
      <p class="hero-text">Corvantis Portal helps undergraduates and healthcare professionals to learn or update their knowledge about the clinically relevant anatomy, ophthalmic examination techniques and common eye disorders of the human eye.</p>
    </div>
    <a class="cta" href="#" style="top:266px">UNDERGRADUATES<strong>LEARN MORE</strong></a>
    <a class="cta" href="#" style="top:332px">HEALTHCARE PROFESSIONALS<strong>LEARN MORE</strong></a>
  </section>

  <div class="trusted"><span class="trusted-rule"></span><span class="trusted-label">TRUSTED ACROSS THE WORLD</span><span class="trusted-rule"></span></div>

  <div class="partners">
    <div class="partner" style="left:180px;top:10px;width:150px"><span class="partner-mark round"></span>Halvorsen College of Eye Surgeons</div>
    <div class="partner" style="left:370px;top:16px"><span class="partner-mark"></span>University of<br>Marlowe</div>
    <div class="partner" style="left:640px;top:16px"><span class="partner-mark"></span>University of<br>Eastmere</div>
    <div class="partner" style="left:826px;top:16px"><span class="partner-mark round"></span>Thornbury School<br>of Medicine</div>
  </div>
</div>
</body>
</html>
```